Brivanta.com the Free Online Tutorial Needs a New Web Design

We need a new web design for our existing website, Brivanta.com. We provide a Free Online Tutorial of any code, like HTML, CSS, PHP, Jquery, javascript etc, including online editor.
We would like to see designs that interesting, simple, interactive, and be a very comfortable place to read in a long time.
We need 2 pages design for:
1. Home Page (http://brivanta.com) and
2. Listing Page (http://brivanta.com/tutorial/833/sql/sql-basics/sql-and-or-operator.html)
For Listing Page We need nice "Left Menu" at left side and Content Page (min 728px) at right side.
I need File PSD and/or Vector Only, without HTML code.
Online
2 page

```html
<!DOCTYPE html>
<html lang="en">
<head>
<meta charset="UTF-8">
<title>Brivanta – HTML5 Introduction</title>
<link rel="stylesheet" href="https://fonts.googleapis.com/css2?family=Oswald:wght@300;400;500&family=Open+Sans:wght@400;600&family=Arimo:wght@400;700&display=swap">
<style>
:root{
  --nav-bg:#2f2f2f;
  --yellow:#fdb813;
  --yellow-dark:#e9a400;
  --green:#6db33f;
  --green-dark:#5a9c2f;
  --red:#e94e4d;
  --page-bg:#eceef0;
  --menu-bg:#3d3d3d;
  --menu-line:#555;
  --ink:#333;
  --ink-soft:#555;
  --white:#fff;
  --footer-bg:#3c3c3c;
  --footer-base:#2a2a2a;
  --footer-text:#d6d6d6;
  --code-blue:#1f6fd1;
  --code-orange:#f29b16;
  --code-red:#d9362b;
  --pill:#dcdcdc;
}
*{box-sizing:border-box;margin:0;padding:0}
html,body{width:1200px;height:2703px;overflow:hidden}
body{position:relative;background:var(--page-bg);font-family:"Arimo",Arial,sans-serif;color:var(--ink)}
.abs{position:absolute}
ul{list-style:none}

/* top navigation */
.topbar{left:0;top:0;width:1200px;height:90px;background:var(--nav-bg)}
.brand{left:110px;top:20px;display:flex;align-items:center;gap:12px}
.brand-square{width:46px;height:46px;background:var(--yellow)}
.brand-name{font-family:"Oswald",sans-serif;font-weight:400;font-size:40px;color:var(--white);line-height:1}
.main-nav{left:406px;top:32px;display:flex;align-items:center;font-family:"Oswald",sans-serif;font-size:17px;color:var(--white)}
.main-nav li{padding:0 13px;border-right:1px solid #8a8a8a;line-height:18px}
.main-nav li:last-child{border-right:none}
.main-nav .active{color:var(--yellow)}
.signup{left:984px;top:25px;width:106px;height:40px;background:var(--yellow);border-radius:3px;font-family:"Oswald",sans-serif;font-size:22px;color:#222;text-align:center;line-height:40px}

/* yellow strip */
.lessonbar{left:0;top:90px;width:1200px;height:50px;background:var(--yellow)}
.lessonbar h1{position:absolute;left:110px;top:8px;font-family:"Oswald",sans-serif;font-weight:400;font-size:26px;color:#2a2a2a}
.search{display:flex}
.search-input{background:#f1f1f1;color:#888;font-size:14px;padding-left:16px;display:flex;align-items:center}
.search-btn{background:var(--green);display:flex;align-items:center;justify-content:center}
.lessonbar .search{position:absolute;left:733px;top:11px;height:32px}
.lessonbar .search-input{width:308px}
.lessonbar .search-btn{width:49px}

/* hero */
.hero{left:0;top:140px;width:1200px;height:298px;background:linear-gradient(90deg,#5d6062 0%,#8b8f91 18%,#c9cccd 38%,#e4e5e5 60%,#eeeeee 100%)}

/* sidebar */
.menu{left:110px;width:229px;background:var(--menu-bg);border-radius:3px;overflow:hidden}
.menu h2{background:var(--yellow);height:42px;font-family:"Oswald",sans-serif;font-weight:400;font-size:22px;color:#222;padding:4px 20px;margin-bottom:5px}
.menu li{height:28px;line-height:27px;padding-left:20px;font-size:13px;color:var(--white);border-bottom:1px solid var(--menu-line)}
.menu li:last-child{border-bottom:none}
.menu li.current{background:var(--red)}

/* content */
.article{left:378px;top:461px;width:712px;height:1346px;background:var(--white)}
.article-title{height:45px;background:var(--green);color:var(--white);font-family:"Oswald",sans-serif;font-weight:400;font-size:27px;padding:3px 18px}
.article-body{padding:0 24px 0 22px}
.article p{font-size:12.3px;line-height:20.7px;color:var(--ink)}
.article h3{font-family:"Oswald",sans-serif;font-weight:300;font-size:28px;color:#222}
.intro{margin-top:24px}
.h-html5{margin-top:28px}
.p-html5{margin-top:10px}
.h-new{margin-top:19px}
.news{margin-top:14px}
.news li{height:28px;font-size:12.3px;line-height:28px;padding-left:27px;position:relative}
.news li::before{content:"›";position:absolute;left:2px;color:#888;font-size:15px}
code{font-family:inherit;background:var(--pill);border-radius:9px;padding:1px 4px}

.promo{left:8px;top:813px;width:689px;height:85px;background:#e4e4e4;display:flex;align-items:center;padding:0 18px;gap:16px}
.promo-mark{width:50px;height:50px;background:#2a2a2a}
.promo-text{font-family:"Open Sans",sans-serif;font-size:32px;color:#222}
.promo-quote{margin-left:auto;font-family:"Open Sans",sans-serif;font-size:14px;font-style:italic;color:#333;line-height:16px}
.promo-btn{background:#3a3a3a;color:var(--white);font-size:13px;font-weight:700;padding:10px 16px;border-radius:2px}

.h-example{left:22px;top:938px}
.codebox{left:20px;top:998px;width:672px;height:262px;border:3px solid var(--code-orange);border-radius:4px;padding:16px 0 0 17px;font-size:11.5px;line-height:22px;color:#222}
.codebox .i{padding-left:10px}
.c-blue{color:var(--code-blue)}
.c-orange{color:var(--code-orange)}
.c-red{color:var(--code-red)}
.try{left:20px;top:1287px;width:106px;height:36px;background:var(--yellow);border-radius:3px;font-family:"Oswald",sans-serif;font-size:19px;text-align:center;line-height:36px;color:#222}

/* ads */
.ad-shoes{left:378px;top:1841px;width:348px;height:287px;background:linear-gradient(90deg,#f28c1c 0 30%,#ffffff 30% 100%)}
.ad-social{left:744px;top:1841px;width:346px;height:287px;background:linear-gradient(180deg,#3b5998 0 12%,#b9a48f 12% 60%,#ffffff 60% 100%)}

/* footer */
.footer-band{left:0;top:2164px;width:1200px;height:56px;background:var(--yellow)}
.footer-band .search{position:absolute;left:110px;top:11px;height:34px}
.footer-band .search-input{width:310px;background:#fafafa}
.footer-band .search-btn{width:45px;border-radius:0 3px 3px 0}
.social{position:absolute;left:938px;top:13px;display:flex;gap:12px}
.footer{left:0;top:2220px;width:1200px;height:416px;background:var(--footer-bg)}
.footer-col{top:42px;color:var(--footer-text)}
.footer-col h4{font-family:"Open Sans",sans-serif;font-weight:400;font-size:19px;color:var(--white);margin-bottom:26px}
.footer-col li{font-family:"Open Sans",sans-serif;font-size:13px;height:28px;line-height:28px}
.base{left:0;top:2636px;width:1200px;height:67px;background:var(--footer-base);font-family:"Open Sans",sans-serif;font-size:13px;color:var(--footer-text)}
.base-links{position:absolute;left:112px;top:24px;display:flex;gap:12px}
.copyright{position:absolute;right:110px;top:24px}
</style>
</head>
<body>

<header class="abs topbar">
  <div class="abs brand"><span class="brand-square"></span><span class="brand-name">Brivanta</span></div>
  <ul class="abs main-nav">
    <li>HOME</li><li class="active">HTML</li><li>CSS</li><li>JAVASCRIPT</li><li>PHP</li><li>SQL</li><li>JQUERY</li><li>JSON</li><li>MORE</li>
  </ul>
  <div class="abs signup">Sign Up</div>
</header>

<div class="abs lessonbar">
  <h1>800 HTML Lessons &amp; Examples</h1>
  <div class="search">
    <div class="search-input">Search Lessons</div>
    <div class="search-btn"><svg width="20" height="20" viewBox="0 0 20 20"><circle cx="8" cy="8" r="6" fill="none" stroke="#fff" stroke-width="2.5"/><line x1="12.5" y1="12.5" x2="18" y2="18" stroke="#fff" stroke-width="3" stroke-linecap="round"/></svg></div>
  </div>
</div>

<div class="abs hero" role="img" aria-label="Photo of a man in a grey shirt and tie writing HTML code on a glass board"></div>

<nav class="abs menu" style="top:465px">
  <h2>HTML5 Tutorials</h2>
  <ul>
    <li>HTML5 Basics</li><li class="current">HTML5 Introduction</li><li>HTML5 New Elements</li><li>HTML5 Syntax</li><li>HTML5 CSS</li><li>&lt;!DOCTYPE&gt;</li><li>!-- comment --</li><li>HTML5 URL Encoding</li><li>HTML5 Entities and Symbols</li><li>HTML5 Standard Attributes</li><li>HTML5 Event Attributes</li><li>HTML5 Unsupported</li><li>HTML5 The Basic of Page</li><li>HTML5 Basic Examples</li>
  </ul>
</nav>

<nav class="abs menu" style="top:941px">
  <h2>HTML5 Head</h2>
  <ul>
    <li>Head Overview</li><li>&lt;base&gt;</li><li>&lt;link&gt;</li><li>&lt;meta&gt;</li><li>&lt;script&gt;</li><li>&lt;style&gt;</li><li>&lt;title&gt;</li>
  </ul>
</nav>

<nav class="abs menu" style="top:1225px">
  <h2>HTML5 Structural</h2>
  <ul>
    <li>Structural Overview</li><li>&lt;!--comment--&gt;</li><li>&lt;article&gt;</li><li>&lt;aside&gt;</li><li>&lt;blockquote&gt;</li><li>&lt;body&gt;</li><li>&lt;br&gt;</li><li>&lt;command&gt;</li><li>&lt;details&gt;</li><li>&lt;div&gt;</li><li>&lt;figcaption&gt;</li><li>&lt;figure&gt;</li><li>&lt;footer&gt;</li><li>&lt;h1&gt;&nbsp;&nbsp;To&nbsp;&nbsp;&lt;h6&gt;</li><li>&lt;head&gt;</li><li>&lt;header&gt;</li><li>&lt;hgroup&gt;</li><li>&lt;hr&gt;</li><li>&lt;html&gt;</li><li>&lt;mark&gt;</li><li>&lt;meter&gt;</li><li>&lt;nav&gt;</li><li>&lt;p&gt;</li><li>&lt;progress&gt;</li><li>&lt;rp&gt;</li><li>&lt;rt&gt;</li><li>&lt;ruby&gt;</li><li>&lt;section&gt;</li><li>&lt;summary&gt;</li><li>&lt;time&gt;</li><li>&lt;wbr&gt;</li>
  </ul>
</nav>

<main class="abs article">
  <h2 class="article-title">HTML5 Introduction</h2>
  <div class="article-body">
    <p class="intro">HTML is the language for describing the structure of Web pages. HTML stands for HyperText Markup Language. Web pages consist of markup tags and plain text. HTML is written in the form of HTML elements consisting of tags enclosed in angle brackets (like &lt;html&gt;). HTML tags most commonly come in pairs like &lt;h1&gt; and &lt;/h1&gt;, although some tags represent empty elements and so are unpaired, for example &lt;img&gt;. The first tag in a pair is the start tag, and the second tag is the end tag (they are also called opening tags and closing tags).</p>
    <h3 class="h-html5">HTML5</h3>
    <p class="p-html5">HTML5 will soon be the standard for web pages and supported in the latest browsers. HTML5 will be the new standard for HTML, XHTML, and the HTML DOM. HTML5 is not something completely new. Most of HTML5 specifications came from HTML 4 or XHTML 1.0.<br>A web browser can read HTML files and compose them into visible or audible web pages. The browser does not display the HTML tags, but uses them to interpret the content of the page. HTML describes the structure of a website semantically along with cues for presentation, making it a markup language rather than a programming language.</p>
    <h3 class="h-new">What is New in HTML5?</h3>
    <ul class="news">
      <li>The DOCTYPE declaration for HTML5 is very simple, <code>&lt;!DOCTYPE html&gt;</code></li>
      <li>The character encoding (charset) declaration is also very simple, <code>&lt;meta charset="UTF-8"&gt;</code></li>
      <li>New Functions for embedding audio <code>&lt;audio&gt;</code>, video <code>&lt;video&gt;</code>, and graphics <code>&lt;svg&gt; and &lt;canvas&gt;</code></li>
      <li>Client-side data storage</li>
      <li>Interactive documents</li>
      <li>New structural elements <code>&lt;article&gt;</code>, <code>&lt;header&gt;</code>, <code>&lt;footer&gt;</code>, <code>&lt;nav&gt;</code>, <code>&lt;section&gt;</code>, and <code>&lt;figure&gt;</code></li>
      <li>New form controls calendar, date, time, email, url, search</li>
      <li>JavaScript enhancements</li>
      <li>New HTML5 API's (Application Programming Interfaces). The most interesting new API's are: HTML Geolocation,</li>
      <li>HTML Drag and Drop, HTML Local Storage, HTML Application Cash, HTML Web Workers, HTML SSE</li>
      <li>HTML5 also includes new elements for better structure, drawing, media content, and better form handling</li>
    </ul>
  </div>

  <div class="abs promo">
    <span class="promo-mark"></span>
    <span class="promo-text">A website in 3 minutes!</span>
    <span class="promo-quote">"The Future"<br>Nextwave</span>
    <span class="promo-btn">FIND OUT HOW</span>
  </div>

  <h3 class="abs h-example">HTML5 Example</h3>
  <div class="abs codebox">
    <div>&lt;!DOCTYPE html&gt;</div>
    <div class="c-blue">&lt;html&gt;</div>
    <div class="c-blue">&lt;head&gt;</div>
    <div class="i">&lt;meta charset="UTF-8"&gt;</div>
    <div class="i c-orange">&lt;title&gt;Title of the document goes here..&lt;/title&gt;</div>
    <div class="c-blue">&lt;/head&gt;</div>
    <div class="c-red">&lt;body&gt;</div>
    <div>Content of the document goes here..</div>
    <div class="c-red">&lt;/body&gt;</div>
    <div class="c-blue">&lt;/html&gt;</div>
  </div>
  <div class="abs try">Try Now</div>
</main>

<aside class="abs ad-shoes" role="img" aria-label="Advertisement for Strideway shoes with a discount offer from shopnest"></aside>
<aside class="abs ad-social" role="img" aria-label="Advertisement for Friendloop social network showing a grid of member photos and a sign up button"></aside>

<div class="abs footer-band">
  <div class="search">
    <div class="search-input">Search Lessons</div>
    <div class="search-btn"><svg width="20" height="20" viewBox="0 0 20 20"><circle cx="8" cy="8" r="6" fill="none" stroke="#fff" stroke-width="2.5"/><line x1="12.5" y1="12.5" x2="18" y2="18" stroke="#fff" stroke-width="3" stroke-linecap="round"/></svg></div>
  </div>
  <div class="social">
    <svg width="30" height="30"><circle cx="15" cy="15" r="13" fill="none" stroke="#fff" stroke-width="2"/></svg>
    <svg width="30" height="30"><circle cx="15" cy="15" r="13" fill="none" stroke="#fff" stroke-width="2"/></svg>
    <svg width="30" height="30"><circle cx="15" cy="15" r="13" fill="none" stroke="#fff" stroke-width="2"/></svg>
    <svg width="30" height="30"><circle cx="15" cy="15" r="13" fill="none" stroke="#fff" stroke-width="2"/></svg>
  </div>
</div>

<footer class="abs footer">
  <div class="abs footer-col" style="left:110px">
    <h4>Random HTML5</h4>
    <ul><li>bdo tag in html5</li><li>html in html5</li><li>dir html5</li><li>style in HTML5</li><li>HTML5 Currency Symbols</li><li>ins tag in html5</li><li>del tag in html5</li><li>td tag in html</li><li>frameset</li><li>sup tag in html5</li></ul>
  </div>
  <div class="abs footer-col" style="left:360px">
    <h4>Random Canvas</h4>
    <ul><li>Canvas Image Loader</li><li>Canvas Pattern</li><li>Canvas Line Join</li><li>Canvas Text Basics</li><li>Canvas Introduction</li><li>Canvas Polyline</li><li>Canvas Line Color</li><li>Canvas Line Cap</li><li>Canvas Semicircles</li><li>html5-canvas-rounded-corn..</li></ul>
  </div>
  <div class="abs footer-col" style="left:632px">
    <h4>Random Java Script</h4>
    <ul><li>JS Global decodeURI()</li><li>JS DOM Form Object</li><li>JS Number Max_Value</li><li>JS RegExp test()</li><li>JS DOM Button Object</li><li>JS Number Positive_Infini..</li><li>Javascript Constructor</li><li>JS String-HTML small()</li><li>JS DOM Input Reset</li><li>JS DOM Anchor Object</li></ul>
  </div>
  <div class="abs footer-col" style="left:890px">
    <h4>Random Articles</h4>
    <ul><li>How to get of everything ..</li><li>How to Make Sitemap.xml</li><li>How to Make Drop Down Men..</li><li>How to make WHOIS lookups..</li><li>Changing text with innerh..</li><li>How to Auto Select All Te..</li><li>How to get an input text ..</li><li>Create Transparency Anima..</li><li>How to Make Drop Down Men..</li><li>How to Make SQL Syntax Hi..</li></ul>
  </div>
</footer>

<div class="abs base">
  <div class="base-links"><span>Terms</span><span>Privacy</span><span>Disclaimer</span><span>Contact</span><span>FAQ</span></div>
  <div class="copyright">Brivanta © 2015, All rights reserved</div>
</div>

</body>
</html>
```